Need Modern Elegant Professional Invoice Design

Need modern elegant professional invoice design along with a second page for time and expense log for professional services

```html
<!DOCTYPE html>
<html lang="en">
<head>
<meta charset="utf-8">
<title>Invoice and Time &amp; Expense Report</title>
<link href="https://fonts.googleapis.com/css2?family=Open+Sans:wght@400;600;700&display=swap" rel="stylesheet">
<style>
  :root{
    --purple:#4a2ea6;
    --orange:#e8863a;
    --orange-soft:#efa363;
    --ink:#2b2b2b;
    --paper:#f5f5f5;
    --backdrop:#e3e4e6;
    --row-blue:#dde3ef;
    --row-grey:#b9b9b9;
    --row-light:#ececec;
    --rule:#7a6cc4;
    --grid:#8f8f8f;
  }
  *{box-sizing:border-box;margin:0;padding:0}
  html,body{width:1200px;height:900px;overflow:hidden}
  body{background:var(--backdrop);font-family:"Open Sans",Arial,sans-serif;color:var(--ink);position:relative}
  .page{position:absolute;top:55px;width:560px;height:790px;background:var(--paper);box-shadow:0 2px 6px rgba(0,0,0,.18);overflow:hidden}
  .page--timesheet{left:30px}
  .page--invoice{left:610px}
  .corner{position:absolute;left:0;top:0}
  .corner--bottom{left:auto;right:0;top:auto;bottom:0}
  .abs{position:absolute}
  .brand{display:flex;align-items:center;gap:8px;color:var(--purple);font-weight:700;font-size:21px;letter-spacing:.5px;white-space:nowrap}
  .brand__dot{width:16px;height:16px;border-radius:50%;background:var(--orange)}
  .doc-title{font-size:21px;text-align:center;line-height:27px;color:#333}
  .fields{left:101px;top:94px;font-size:10px;line-height:20.7px}
  .field{display:flex;width:188px}
  .field span{flex:1;border-bottom:1px solid #444;margin:0 0 5px 3px}
  .period{left:338px;top:116px;width:132px;border:1px solid var(--grid);font-size:9px;border-collapse:collapse}
  .period th{background:var(--purple);color:#fff;font-weight:400;height:14px}
  .period td{border:1px solid var(--grid);padding:0 5px;height:14px}
  table{border-collapse:collapse;table-layout:fixed}
  .expenses{left:68px;top:178px;width:424px;font-size:9.5px}
  .expenses th{background:var(--purple);color:#fff;font-weight:600;height:19px;text-align:left;padding-left:8px}
  .expenses td{height:19px;border:1px solid var(--rule)}
  .expenses tbody tr:nth-child(odd) td{background:var(--row-blue)}
  .expenses tfoot td{background:var(--orange);color:#fff;border-color:var(--orange);padding-left:6px}
  .week{left:68px;top:454px;width:424px;font-size:9px}
  .week th{background:var(--purple);color:#fff;font-weight:400;text-align:left;padding:0 5px;height:28px;line-height:12px;vertical-align:middle}
  .week td{border:1px solid var(--grid);height:14px;padding:0 5px;line-height:13px}
  .week td:last-child{background:#cfcfcf}
  .week .row-hours td{background:var(--orange);height:28px}
  .week .row-hours td:first-child,.week .row-pay td:first-child{background:var(--paper)}
  .week .row-hours td:last-child{background:#cfcfcf}
  .week .row-pay td{height:28px}
  .sign{width:150px;text-align:center;font-size:9.5px;border-top:1px solid #555;padding-top:16px}
  .invoice-word{left:354px;top:52px;font-size:42px;line-height:50px;color:#222;letter-spacing:1px}
  .bill-to{left:68px;top:138px;width:167px;border:1px solid var(--orange);font-size:9.5px;line-height:14px}
  .bill-to h4{background:var(--orange);color:#222;font-weight:400;padding-left:5px}
  .bill-to p{padding:0 5px 2px}
  .meta{left:364px;top:137px;width:154px;font-size:9.5px}
  .meta td{border:1px solid var(--grid);padding:0 5px;height:14px}
  .items{left:68px;top:229px;width:454px;font-size:9.5px;text-align:center}
  .items th{background:var(--purple);color:#fff;font-weight:600;height:30px}
  .items td{height:27.6px;border-right:2px solid var(--paper)}
  .items tbody tr:nth-child(odd) td{background:var(--row-grey)}
  .items tbody tr:nth-child(even) td{background:var(--row-light)}
  .items tbody td:first-child{background:#d4d4d4 !important;font-weight:600}
  .totals{left:364px;top:521px;width:154px;font-size:9.5px}
  .totals td{height:22px;border:1px solid var(--orange);padding:0 5px}
  .totals td:last-child{text-align:right}
  .totals .is-orange td:first-child{background:var(--orange)}
  .totals .is-purple td:first-child{background:var(--purple);color:#fff}
  .totals .is-purple td{border-color:var(--purple)}
  .label-orange{color:var(--orange);font-weight:600}
  .payment{left:62px;top:544px;font-size:9.5px;line-height:14px}
  .terms{left:56px;top:627px;width:218px;font-size:9px;line-height:11.6px}
</style>
</head>
<body>

<section class="page page--timesheet">
  <svg class="corner" width="110" height="360" viewBox="0 0 110 360" aria-hidden="true">
    <polygon points="0,0 100,0 0,340" fill="var(--orange-soft)"/>
    <polygon points="0,0 56,0 0,330" fill="var(--purple)"/>
  </svg>

  <div class="brand abs" style="left:106px;top:36px"><span class="brand__dot"></span>Vantage Adjusters</div>
  <h1 class="doc-title abs" style="left:330px;top:22px;width:180px;font-weight:400">Time &amp; Expense<br>Report</h1>

  <div class="fields abs">
    <div class="field">Name<span></span></div>
    <div class="field">Employee ID<span></span></div>
    <div class="field">Department<span></span></div>
    <div class="field">Manager<span></span></div>
  </div>

  <table class="period abs">
    <tr><th colspan="2">PERIOD</th></tr>
    <tr><td style="width:40%">From</td><td>##/##/####</td></tr>
    <tr><td>To</td><td>##/##/####</td></tr>
  </table>

  <table class="expenses abs">
    <colgroup><col style="width:15.5%"><col style="width:48.8%"><col style="width:18.9%"><col></colgroup>
    <thead><tr><th style="padding-left:22px">Date</th><th>Description</th><th>Expense Type</th><th>Amount</th></tr></thead>
    <tbody>
      <tr><td></td><td></td><td></td><td></td></tr>
      <tr><td></td><td></td><td></td><td></td></tr>
      <tr><td></td><td></td><td></td><td></td></tr>
      <tr><td></td><td></td><td></td><td></td></tr>
      <tr><td></td><td></td><td></td><td></td></tr>
      <tr><td></td><td></td><td></td><td></td></tr>
      <tr><td></td><td></td><td></td><td></td></tr>
      <tr><td></td><td></td><td></td><td></td></tr>
      <tr><td></td><td></td><td></td><td></td></tr>
      <tr><td></td><td></td><td></td><td></td></tr>
      <tr><td></td><td></td><td></td><td></td></tr>
    </tbody>
    <tfoot><tr><td colspan="3">Total Expense</td><td></td></tr></tfoot>
  </table>

  <table class="week abs">
    <colgroup><col style="width:10.4%"><col style="width:11%"><col style="width:13.4%"><col style="width:9.8%"><col style="width:12%"><col style="width:10.9%"><col style="width:10.9%"><col style="width:10.7%"><col></colgroup>
    <thead><tr><th>Day of Week</th><th>Regular (h)mm</th><th>Over time (h)mm</th><th>Sick (h)mm</th><th>Vacation (h)mm</th><th>Holiday (h)mm</th><th>Unpaid</th><th>Other</th><th>Total (h)mm</th></tr></thead>
    <tbody>
      <tr><td>Mon</td><td></td><td></td><td></td><td></td><td></td><td></td><td></td><td></td></tr>
      <tr><td>Tue</td><td></td><td></td><td></td><td></td><td></td><td></td><td></td><td></td></tr>
      <tr><td>Wed</td><td></td><td></td><td></td><td></td><td></td><td></td><td></td><td></td></tr>
      <tr><td>Thu</td><td></td><td></td><td></td><td></td><td></td><td></td><td></td><td></td></tr>
      <tr><td>Fri</td><td></td><td></td><td></td><td></td><td></td><td></td><td></td><td></td></tr>
      <tr><td>Sat</td><td></td><td></td><td></td><td></td><td></td><td></td><td></td><td></td></tr>
      <tr><td>Sun</td><td></td><td></td><td></td><td></td><td></td><td></td><td></td><td></td></tr>
      <tr class="row-hours"><td>Total hrs</td><td></td><td></td><td></td><td></td><td></td><td></td><td></td><td></td></tr>
      <tr class="row-pay"><td>Total pay</td><td></td><td></td><td></td><td></td><td></td><td></td><td></td><td></td></tr>
    </tbody>
  </table>

  <div class="sign abs" style="left:64px;top:734px">Authorized Signature</div>
  <div class="sign abs" style="left:314px;top:734px">Employee Signature</div>
</section>

<section class="page page--invoice">
  <svg class="corner" width="110" height="345" viewBox="0 0 110 345" aria-hidden="true">
    <polygon points="0,0 104,0 0,338" fill="var(--orange-soft)"/>
    <polygon points="0,0 61,0 0,300" fill="var(--purple)"/>
  </svg>
  <svg class="corner corner--bottom" width="100" height="290" viewBox="0 0 100 290" aria-hidden="true">
    <polygon points="6,290 100,0 100,290" fill="var(--orange-soft)"/>
    <polygon points="51,290 100,10 100,290" fill="var(--purple)"/>
  </svg>

  <div class="brand abs" style="left:110px;top:76px"><span class="brand__dot"></span>Vantage Adjusters</div>
  <h1 class="invoice-word abs" style="font-weight:400">INVOICE</h1>

  <div class="bill-to abs">
    <h4>BILL TO</h4>
    <p>Name<br>Street Address<br>City, State, ZIP Code<br>Phone</p>
  </div>

  <table class="meta abs">
    <tr><td style="width:48%">Invoice No</td><td>######</td></tr>
    <tr><td>Date</td><td>######</td></tr>
  </table>

  <table class="items abs">
    <colgroup><col style="width:36px"><col style="width:207px"><col style="width:78px"><col style="width:43px"><col></colgroup>
    <thead><tr><th>SL.</th><th>Item Description</th><th>Price</th><th>Qty</th><th>Total</th></tr></thead>
    <tbody>
      <tr><td>1</td><td>Lorem Ipsum</td><td>50</td><td>1</td><td>50</td></tr>
      <tr><td>2</td><td>Lorem Ipsum</td><td>50</td><td>1</td><td>50</td></tr>
      <tr><td>3</td><td>Lorem Ipsum</td><td>50</td><td>1</td><td>50</td></tr>
      <tr><td>4</td><td>Lorem Ipsum</td><td>50</td><td>1</td><td>50</td></tr>
      <tr><td>5</td><td>Lorem Ipsum</td><td>50</td><td>1</td><td>50</td></tr>
      <tr><td></td><td></td><td></td><td></td><td></td></tr>
      <tr><td></td><td></td><td></td><td></td><td></td></tr>
      <tr><td></td><td></td><td></td><td></td><td></td></tr>
      <tr><td></td><td></td><td></td><td></td><td></td></tr>
    </tbody>
  </table>

  <table class="totals abs">
    <tr class="is-orange"><td style="width:48%">Sub Total</td><td>######</td></tr>
    <tr><td>Tax</td><td>######</td></tr>
    <tr class="is-orange"><td>Discount</td><td>######</td></tr>
    <tr class="is-purple"><td>Total</td><td>########</td></tr>
  </table>

  <div class="payment abs">
    <div class="label-orange">Payment Info</div>
    Account : 123 456 789<br>A/C Name : Lorem Ipsum<br>Bank Details : Lorem Ipsum
  </div>

  <div class="terms abs">
    <div class="label-orange" style="font-size:10px">Terms and Conditions</div>
    Lorem Ipsum is simply dummy text of the printing and typesetting industry. Lorem Ipsum has been the industry's standard dummy text ever since the 1500s, when an unknown printer took a galley of type and scrambled it to make a type specimen book.
  </div>

  <div class="sign abs" style="left:314px;top:691px">Authorized Signature</div>
</section>

</body>
</html>
```